Hedge fund needs power point design for marketing pitch

We need a designer to make our power point pitch more aesthetically appealing to potential clients. We will be marketing our hedge fund to high net worth individuals and financial institutions. The ideal design will look professional and project confidence to our potential clients. We have attached a rough outline of what we have completed so far. We have also attached example cover pages for 2 pitch books produced by our competitors.

Target Market(s)

Financial institutions and wealthy investors

Industry/Entity Type

Finance

Requirements
Must have
• must use our logo and current slides. Must look professional

```html
<!DOCTYPE html>
<html lang="en">
<head>
<meta charset="utf-8">
<title>Marlowe Capital Management – Pitch Deck Slides</title>
<link href="https://fonts.googleapis.com/css2?family=Open+Sans:wght@300;400;600;700&display=swap" rel="stylesheet">
<style>
  :root {
    --stage: #e9e6df;
    --green-deep: #0b2517;
    --green: #12351f;
    --gold: #d4a92c;
    --gold-light: #f3d774;
    --gold-dark: #b88a1a;
    --ink: #1d1d1d;
    --ink-soft: #333;
    --white: #ffffff;
    --cream: #f2ead2;
  }
  * { box-sizing: border-box; margin: 0; padding: 0; }
  html, body { width: 1200px; height: 900px; overflow: hidden; }
  body {
    background: var(--stage);
    font-family: "Open Sans", Arial, sans-serif;
    position: relative;
  }
  .slide {
    position: absolute;
    width: 520px;
    height: 390px;
    overflow: hidden;
    box-shadow: 0 6px 16px rgba(0,0,0,0.18);
  }
  .slide--cover   { left: 60px;  top: 40px; }
  .slide--objective { left: 620px; top: 40px; }
  .slide--strategy  { left: 60px;  top: 470px; }
  .slide--contact   { left: 620px; top: 470px; }

  .slide--dark {
    background: radial-gradient(ellipse at 50% 45%, #16402a 0%, var(--green) 55%, var(--green-deep) 100%);
    color: var(--white);
    text-align: center;
  }
  .slide--light { background: var(--white); color: var(--ink); }

  .top-arc { position: absolute; left: 0; top: 0; width: 520px; height: 50px; }

  .brand { position: absolute; left: 0; right: 0; }
  .brand__name {
    font-weight: 600;
    font-size: 28px;
    letter-spacing: 3px;
    color: var(--gold);
    line-height: 1;
  }
  .brand__sub {
    margin-top: 6px;
    font-size: 12.5px;
    letter-spacing: 0.3px;
    color: var(--white);
  }
  .rule {
    position: absolute;
    left: 70px; right: 70px;
    height: 1px;
    background: linear-gradient(90deg, transparent, var(--gold) 30%, var(--gold) 70%, transparent);
  }
  .cover-line {
    position: absolute; left: 0; right: 0;
    font-weight: 300;
    font-size: 16px;
    color: var(--cream);
  }

  .footer {
    position: absolute;
    left: 0; right: 0;
    top: 362px;
    height: 15px;
    background: linear-gradient(90deg, var(--gold-dark), var(--gold-light) 55%, var(--gold));
    display: flex;
    justify-content: space-between;
    align-items: center;
    padding: 0 10px;
    font-size: 7.5px;
    color: var(--green-deep);
  }
  .footer-base {
    position: absolute; left: 0; right: 0; top: 377px; bottom: 0;
    background: var(--green);
  }
  .slide--light .footer-base { background: var(--white); }
  .page-num {
    position: absolute;
    top: 359px;
    width: 21px; height: 21px;
    border-radius: 50%;
    background: var(--white);
    border: 1px solid var(--gold-dark);
    font-size: 13px;
    line-height: 19px;
    text-align: center;
    color: var(--ink);
  }

  .slide-title {
    position: absolute;
    font-weight: 600;
    font-size: 24px;
    color: #2b2b2b;
    line-height: 1;
  }
  .title-rule {
    position: absolute; left: 0; right: 0; height: 1px;
    background: linear-gradient(90deg, rgba(212,169,44,0.3), var(--gold) 40%, rgba(212,169,44,0.2));
  }
  .photo {
    position: absolute;
    top: 0;
  }
  .photo--climb {
    right: 0; width: 190px; height: 230px;
    background: radial-gradient(ellipse at 85% 20%, #8d9097 0%, #b9bcc3 35%, rgba(230,232,236,0.6) 65%, rgba(255,255,255,0) 85%);
  }
  .photo--chess {
    right: 0; width: 250px; height: 165px;
    background: radial-gradient(ellipse at 65% 40%, #d9d9d9 0%, #e8e8e8 40%, rgba(245,245,245,0.6) 65%, rgba(255,255,255,0) 85%);
  }

  .points { position: absolute; list-style: none; font-size: 16px; line-height: 20px; color: var(--ink-soft); }
  .points > li { position: relative; padding-left: 21px; }
  .points > li::before {
    content: "";
    position: absolute; left: 0; top: 4px;
    width: 11px; height: 11px; border-radius: 50%;
    border: 3px solid var(--gold);
    background: #3a3a1a;
  }
  .sub-points { list-style: none; padding-left: 17px; }
  .sub-points li { position: relative; padding-left: 11px; }
  .sub-points li::before {
    content: ""; position: absolute; left: 0; top: 8px;
    width: 5px; height: 5px; border-radius: 50%; background: var(--ink);
  }
  .points--objective { left: 32px; top: 104px; width: 470px; }
  .points--objective > li + li { margin-top: 20px; }
  .points--strategy { left: 32px; top: 105px; width: 470px; }

  .contact-heading {
    position: absolute; left: 0; right: 0; top: 213px;
    font-weight: 600; font-size: 17px; color: var(--white);
  }
  .contact-lines {
    position: absolute; left: 0; right: 0;
    font-weight: 300; font-size: 13px; line-height: 16.5px; color: var(--cream);
  }
</style>
</head>
<body>

  <!-- Cover -->
  <section class="slide slide--dark slide--cover">
    <svg class="top-arc" viewBox="0 0 520 50" aria-hidden="true">
      <defs>
        <linearGradient id="arcGoldA" x1="0" x2="1">
          <stop offset="0" stop-color="#b88a1a"/><stop offset="0.5" stop-color="#f3d774"/><stop offset="1" stop-color="#c99a22"/>
        </linearGradient>
      </defs>
      <path d="M0 0 H520 V4 Q260 80 0 4 Z" fill="url(#arcGoldA)"/>
      <path d="M0 0 H520 V0 Q260 68 0 0 Z" fill="#0d2c1a"/>
    </svg>
    <div class="brand" style="top:131px;">
      <div class="brand__name">MARLOWE</div>
      <div class="brand__sub">CAPITAL MANAGEMENT LLC</div>
    </div>
    <div class="rule" style="top:195px;"></div>
    <p class="cover-line" style="top:212px;">Marlowe Derivatives Fund LP</p>
    <p class="cover-line" style="top:256px;">Confidential</p>
    <p class="cover-line" style="top:299px;">April 2016</p>
    <div class="footer">
      <span>Marlowe Capital Management LLC Copyright 2016©</span>
      <span>www.marlowecapital.com</span>
    </div>
    <div class="footer-base"></div>
  </section>

  <!-- Investment Objective -->
  <section class="slide slide--light slide--objective">
    <div class="photo photo--climb" role="img" aria-label="Photo of a rock climber scaling a cliff against a pale sky"></div>
    <h2 class="slide-title" style="left:41px; top:18px;">Investment Objective</h2>
    <div class="title-rule" style="top:63px;"></div>
    <ul class="points points--objective">
      <li>Profit from inefficiencies in equity and index options markets
        <ul class="sub-points">
          <li>Buy options that are underpriced</li>
          <li>Sell options that are overpriced</li>
        </ul>
      </li>
      <li>Achieve outsized and consistent returns by maintaining a small and nimble fund that can exploit price inefficiencies and move in and out of trades quickly</li>
    </ul>
    <div class="footer">
      <span>www.marlowecapital.com</span>
      <span></span>
    </div>
    <div class="footer-base"></div>
    <div class="page-num" style="left:480px;">1</div>
  </section>

  <!-- Investment Strategy -->
  <section class="slide slide--light slide--strategy">
    <div class="photo photo--chess" role="img" aria-label="Photo of chess pieces on a faded chessboard"></div>
    <h2 class="slide-title" style="left:41px; top:18px;">Investment Strategy</h2>
    <div class="title-rule" style="top:64px;"></div>
    <ul class="points points--strategy">
      <li>Strategy derived from a dynamic optimization problem that maximizes returns within a given risk constraint. Parameters/assumptions
        <ul class="sub-points">
          <li>Assume liquid markets</li>
          <li>Assume a price discount/premium on each trade (5-10%)</li>
        </ul>
      </li>
      <li>Solution - the optimization problem tells us:
        <ul class="sub-points">
          <li>When to buy or sell contracts</li>
          <li>Which contracts to buy or sell</li>
          <li>How many contracts to buy or sell</li>
        </ul>
      </li>
      <li>We make trades based on these solutions while hitting the price discount/premium offered by the market.</li>
    </ul>
    <div class="footer">
      <span>www.marlowecapital.com</span>
      <span></span>
    </div>
    <div class="footer-base"></div>
    <div class="page-num" style="left:479px;">2</div>
  </section>

  <!-- Contact -->
  <section class="slide slide--dark slide--contact">
    <svg class="top-arc" viewBox="0 0 520 50" aria-hidden="true">
      <defs>
        <linearGradient id="arcGoldB" x1="0" x2="1">
          <stop offset="0" stop-color="#b88a1a"/><stop offset="0.5" stop-color="#f3d774"/><stop offset="1" stop-color="#c99a22"/>
        </linearGradient>
      </defs>
      <path d="M0 0 H520 V4 Q260 80 0 4 Z" fill="url(#arcGoldB)"/>
      <path d="M0 0 H520 V0 Q260 68 0 0 Z" fill="#0d2c1a"/>
    </svg>
    <div class="brand" style="top:133px;">
      <div class="brand__name">MARLOWE</div>
      <div class="brand__sub">CAPITAL MANAGEMENT LLC</div>
    </div>
    <div class="rule" style="top:195px;"></div>
    <h3 class="contact-heading">Contact Information</h3>
    <p class="contact-lines" style="top:249px;">482 North Cedar Ave, Plano, TX 75093<br>Ph. 5550 12876 Fax. 5550 34219</p>
    <p class="contact-lines" style="top:298px;">email : contact@marlowecapital.com<br>www.marlowecapital.com</p>
    <div class="footer">
      <span>Marlowe Capital Management LLC Copyright 2016©</span>
      <span>www.marlowecapital.com</span>
    </div>
    <div class="footer-base"></div>
  </section>

</body>
</html>
```